Q7M Electrical Systems Inc Business Cards

Target Market(s)

Customers

Industry/Entity Type

Construction - Electrical

Contact Information for Business Card

Company Name, Address, Phone, and email address

Font styles to use
Sans Serif

Colors
0054AA
0677BA
7BADD7
CADEEF
E8F1F8

Requirements
Must have
• we would like to use the same design that we had our vehicles wrapped
Nice to have
• The design that we used on our trucks

```html
<!DOCTYPE html>
<html lang="en">
<head>
<meta charset="utf-8">
<title>Q7M Electrical Systems Inc – Business Cards</title>
<link href="https://fonts.googleapis.com/css2?family=Roboto:wght@700&family=Montserrat:wght@600&display=swap" rel="stylesheet">
<style>
  :root {
    --backdrop: #ec6726;
    --navy: #0c1631;
    --silver: #c2c5c8;
    --paper: #ffffff;
    --trace: #e9eaec;
    --card-shadow: 10px 12px 10px rgba(90, 35, 5, 0.45);
  }
  html, body {
    margin: 0;
    padding: 0;
    width: 923px;
    height: 1200px;
    overflow: hidden;
    background: var(--backdrop);
  }
  .sheet {
    position: relative;
    width: 923px;
    height: 1200px;
  }
  .card {
    position: absolute;
    left: 136px;
    width: 652px;
    height: 373px;
    background: var(--paper);
    box-shadow: var(--card-shadow);
    overflow: hidden;
  }
  .card--front { top: 154px; }
  .card--back { top: 670px; }

  .front-art {
    position: absolute;
    inset: 0;
    width: 100%;
    height: 100%;
  }
  .front-name {
    position: absolute;
    left: 0;
    right: 0;
    top: 118px;
    text-align: center;
    color: var(--navy);
    font-family: "Roboto", Arial, sans-serif;
    font-weight: 700;
    line-height: 1;
  }
  .front-name__mark {
    display: block;
    font-size: 84px;
    letter-spacing: 2px;
  }
  .front-name__rest {
    display: block;
    margin-top: 14px;
    font-size: 24px;
    letter-spacing: 3px;
  }

  .back-trace {
    position: absolute;
    right: 0;
    bottom: 0;
    width: 240px;
    height: 373px;
  }
  .back-title {
    position: absolute;
    left: 49px;
    top: 80px;
    margin: 0;
    color: var(--navy);
    font-family: "Roboto", Arial, sans-serif;
    font-weight: 700;
    font-size: 33px;
    white-space: nowrap;
  }
  .back-title__mark { font-size: 40px; }
  .contact {
    position: absolute;
    left: 52px;
    margin: 0;
    padding: 0;
    list-style: none;
    color: var(--navy);
    font-family: "Montserrat", Arial, sans-serif;
    font-weight: 600;
    font-size: 17px;
    line-height: 21px;
  }
  .contact__item {
    position: absolute;
    left: 0;
    display: flex;
    align-items: center;
    white-space: nowrap;
  }
  .contact__item--address { top: 168px; }
  .contact__item--email { top: 240px; }
  .contact__item--phone { top: 292px; }
  .contact__icon {
    width: 34px;
    height: 34px;
    margin-right: 16px;
    flex: none;
  }
</style>
</head>
<body>
<main class="sheet">
  <section class="card card--front">
    <svg class="front-art" viewBox="0 0 652 373" preserveAspectRatio="none">
      <rect width="652" height="373" fill="var(--navy)" role="img" aria-label="Navy field with a faint circuit-board trace pattern"/>
      <path d="M197,0 L614,0 C640,120 600,280 430,373 L40,373 C30,230 80,90 197,0 Z" fill="var(--silver)"/>
      <path d="M225,0 L545,0 C598,130 560,290 450,373 L108,373 C88,240 120,90 225,0 Z" fill="var(--paper)"/>
      <path d="M540,0 C565,70 568,130 560,200" fill="none" stroke="var(--paper)" stroke-width="5"/>
      <path d="M100,373 C80,300 82,220 110,150" fill="none" stroke="var(--paper)" stroke-width="4"/>
    </svg>
    <div class="front-name">
      <span class="front-name__mark">Q7M</span>
      <span class="front-name__rest">ELECTRICAL SYSTEMS INC</span>
    </div>
  </section>

  <section class="card card--back">
    <svg class="back-trace" viewBox="0 0 240 373" role="img" aria-label="Light grey circuit-board trace pattern">
      <defs>
        <linearGradient id="traceFade" x1="0" y1="1" x2="1" y2="0">
          <stop offset="0" stop-color="var(--trace)"/>
          <stop offset="1" stop-color="var(--paper)"/>
        </linearGradient>
      </defs>
      <polygon points="240,0 240,373 0,373 80,270 140,120 190,40 210,0" fill="url(#traceFade)"/>
    </svg>

    <h1 class="back-title"><span class="back-title__mark">Q7M</span> ELECTRICAL SYSTEM INC</h1>

    <ul class="contact">
      <li class="contact__item contact__item--address">
        <svg class="contact__icon" viewBox="0 0 34 42" aria-hidden="true">
          <path d="M17,1 C8,1 1,8 1,17 C1,28 17,41 17,41 C17,41 33,28 33,17 C33,8 26,1 17,1 Z" fill="var(--navy)"/>
          <circle cx="17" cy="16" r="5.5" fill="var(--paper)"/>
        </svg>
        <span>418 Harlow Bend #207<br>Cedar Hollow, FL 32790</span>
      </li>
      <li class="contact__item contact__item--email">
        <svg class="contact__icon" viewBox="0 0 34 24" aria-hidden="true">
          <rect x="0" y="0" width="34" height="24" rx="2" fill="var(--navy)"/>
          <path d="M2,3 L17,14 L32,3" fill="none" stroke="var(--paper)" stroke-width="2.4"/>
        </svg>
        <span>info@q7melectric.com</span>
      </li>
      <li class="contact__item contact__item--phone">
        <svg class="contact__icon" viewBox="0 0 24 24" aria-hidden="true">
          <path d="M6.6,10.8 C8,13.6 10.4,16 13.2,17.4 L15.4,15.2 C15.7,14.9 16.1,14.8 16.4,15 C17.5,15.4 18.7,15.6 20,15.6 C20.6,15.6 21,16 21,16.6 L21,20 C21,20.6 20.6,21 20,21 C10.6,21 3,13.4 3,4 C3,3.4 3.4,3 4,3 L7.5,3 C8.1,3 8.5,3.4 8.5,4 C8.5,5.3 8.7,6.5 9.1,7.6 C9.2,7.9 9.1,8.3 8.9,8.6 Z" fill="var(--navy)"/>
        </svg>
        <span>407-555-0148</span>
      </li>
    </ul>
  </section>
</main>
</body>
</html>
```